Stationary Design for Stunning new Logo

I need to envelopes, letterhead, business cards designed to compliment our new logo.

We are a 25 year old printing company going through a brand refresh. All items should have the design extended to both sides for full print ability.

Industry/Entity Type

Printing

Requirements
Must have
• It must utilize the new logo & colors PMS 300 & PMS 295.

```html
<!DOCTYPE html>
<html lang="en">
<head>
<meta charset="utf-8">
<title>Talvorin Stationery</title>
<link href="https://fonts.googleapis.com/css2?family=Roboto+Slab:wght@300;400;700&family=Roboto+Condensed:wght@400;700&display=swap" rel="stylesheet">
<style>
  :root {
    --brand-blue: #1b6fb6;
    --brand-navy: #164a7c;
    --ink-soft: #5b6f86;
    --paper: #ffffff;
    --backdrop: #e9e6e1;
  }
  * { margin: 0; padding: 0; box-sizing: border-box; }
  html, body { width: 1200px; height: 1000px; overflow: hidden; }
  body {
    background: var(--backdrop);
    position: relative;
    font-family: "Roboto Slab", Georgia, serif;
    color: var(--brand-blue);
  }
  .sheet {
    position: absolute;
    background: var(--paper);
    overflow: hidden;
    box-shadow: 0 4px 12px rgba(0,0,0,.25);
  }
  .brand { position: absolute; text-align: left; }
  .brand-name {
    font-family: "Roboto Slab", Georgia, serif;
    font-weight: 700;
    color: var(--brand-blue);
    line-height: 1;
    display: flex;
    align-items: center;
    white-space: nowrap;
  }
  .brand-dot {
    display: inline-block;
    flex: none;
    border-radius: 50%;
    background: var(--brand-blue);
  }
  .brand-tagline {
    font-family: "Roboto Condensed", Arial, sans-serif;
    color: var(--brand-blue);
    text-transform: uppercase;
    white-space: nowrap;
  }

  /* Letterhead */
  .letterhead { left: 157px; top: 98px; width: 619px; height: 800px; }
  .letterhead .brand { left: 159px; top: 44px; }
  .letterhead .brand-name { font-size: 33px; letter-spacing: .07em; gap: 8px; }
  .letterhead .brand-dot { width: 38px; height: 38px; }
  .letterhead .brand-tagline { font-size: 9px; margin-top: 1px; margin-left: 46px; }
  .letterhead .footer {
    position: absolute; left: 71px; top: 754px;
    font-size: 11.5px; color: var(--ink-soft); white-space: nowrap; letter-spacing: .03em;
  }
  .footer strong { color: var(--brand-blue); font-weight: 700; }
  .sep { color: var(--brand-navy); margin: 0 5px; }

  /* Envelope */
  .envelope { left: 405px; top: 522px; width: 692px; height: 298px; box-shadow: 0 8px 14px rgba(0,0,0,.35); }
  .envelope .brand { left: 27px; top: 24px; }
  .envelope .brand-name { font-size: 17px; letter-spacing: .06em; gap: 4px; }
  .envelope .brand-dot { width: 20px; height: 20px; }
  .envelope .brand-tagline { font-size: 5px; margin-left: 24px; margin-top: 1px; }
  .envelope .return-address { font-size: 8px; color: var(--ink-soft); margin-left: 24px; margin-top: 4px; letter-spacing: .02em; }

  /* Business card */
  .card-front { left: 806px; top: 174px; width: 254px; height: 146px; }
  .card-front .brand { left: 14px; top: 17px; }
  .card-front .brand-name { font-size: 23px; letter-spacing: .06em; gap: 6px; }
  .card-front .brand-dot { width: 30px; height: 30px; }
  .card-front .brand-tagline { font-size: 6.7px; margin-left: 36px; margin-top: 0; }
  .holder { position: absolute; left: 0; right: 0; top: 63px; text-align: center; }
  .holder-name { font-size: 9px; font-weight: 700; color: var(--brand-navy); letter-spacing: .06em; }
  .holder-title { font-size: 6.5px; color: var(--ink-soft); letter-spacing: .06em; margin-top: 1px; }
  .card-address { position: absolute; left: 18px; top: 101px; font-size: 7.5px; color: var(--ink-soft); line-height: 10px; }
  .card-contact { position: absolute; right: 18px; top: 91px; font-size: 7.5px; color: var(--ink-soft); line-height: 10px; text-align: right; }
  .card-address strong, .card-contact strong { color: var(--brand-blue); font-weight: 700; }

  .card-back {
    left: 808px; top: 349px; width: 254px; height: 145px;
    background: var(--brand-navy);
    display: flex; align-items: center; justify-content: center;
  }
  .card-back .brand-name { color: var(--paper); font-size: 22px; letter-spacing: .06em; gap: 8px; }
  .card-back .brand-dot { background: var(--paper); width: 26px; height: 26px; }
</style>
</head>
<body>

<section class="sheet letterhead">
  <div class="brand">
    <div class="brand-name"><span class="brand-dot"></span>TALVORIN</div>
    <div class="brand-tagline">Outstanding Service • Quality Product • Competitive Pricing.</div>
  </div>
  <p class="footer">1234 Main Street, Town, ST 12345<span class="sep">▪</span><strong>www.talvorin.com</strong><span class="sep">▪</span>p 123.456.7890<span class="sep">▪</span>f 123.456.7890</p>
</section>

<section class="sheet envelope">
  <div class="brand">
    <div class="brand-name"><span class="brand-dot"></span>TALVORIN</div>
    <div class="brand-tagline">Outstanding Service • Quality Product • Competitive Pricing.</div>
    <div class="return-address">1234 Main Street, Town, ST 12345</div>
  </div>
</section>

<section class="sheet card-front">
  <div class="brand">
    <div class="brand-name"><span class="brand-dot"></span>TALVORIN</div>
    <div class="brand-tagline">Outstanding Service • Quality Product • Competitive Pricing.</div>
  </div>
  <div class="holder">
    <div class="holder-name">JOHN SMITH</div>
    <div class="holder-title">PRESIDENT</div>
  </div>
  <div class="card-address">1234 Main Street<br>Town, ST 12345<br><strong>www.talvorin.com</strong></div>
  <div class="card-contact">m&nbsp; 123.456.7890<br>p&nbsp; 123.456.7890<br>f&nbsp; 123.456.7890<br><strong>jsmith@talvorin.com</strong></div>
</section>

<section class="sheet card-back">
  <div class="brand-name"><span class="brand-dot"></span>TALVORIN</div>
</section>

</body>
</html>
```